【テキスト】
ーーーーーーーーーーーーー
(メインタイトル)
黄金羅針盤アカデミー
実践攻略
前編
(サブタイトル)
相続市場を狙え!!
利回り20%&転売益2000万!
ーーーーーーーーーーーーー

【イメージ】
・3つ添付させて頂きました。
・「デザイン2」のように立体的にお願いします。
・文字は横書きでお願いします。

ターゲット:40~50代・男性・会社員:年収1000万
参考LP:https://veltrano-k.jp/lp/seminar1/

【納品形式】
PNGファイル
記載項目
(メインタイトル)
黄金羅針盤アカデミー
実践攻略
前編
(サブタイトル)
相続市場を狙え!!
利回り20%&転売益2000万!
サイズ
• 要相談・教えてください。
希望イメージ
シンプル 複雑
単色 カラフル
暗い 明るい
日常 高級
遊び心 厳粛
未来的 伝統的
女性的 男性的
希望する色
赤系、青系、紫系
納品ファイル
• PNG形式 (.png)
■ 選んだ理由

カラー・フォント・配置がバランス良く感じました。

■ 提案者全員のお礼・コメント

この度は大変お世話になりました。
別案件でまた依頼したいと感じました。

```html
<!DOCTYPE html>
<html lang="ja">
<head>
<meta charset="utf-8">
<title>黄金羅針盤アカデミー 実践攻略 前編</title>
<link href="https://fonts.googleapis.com/css2?family=Noto+Sans+JP:wght@700;900&family=Noto+Serif+JP:wght@700;900&display=swap" rel="stylesheet">
<style>
  :root {
    --page-bg: #ffffff;
    --sky-top: #9ec8ec;
    --sky-mid: #d9ebf8;
    --sky-low: #eef6fc;
    --ink: #1a1a1a;
    --accent-red: #d0101b;
    --panel-white: #ffffff;
    --navy: #14244d;
    --navy-deep: #0a1534;
    --city-haze: #c4d8e8;
    --city-mid: #8aa6bf;
    --city-dark: #566c82;
    --spine-top: #b9d7f0;
    --spine-low: #dbe9f5;
    --white: #ffffff;
  }
  * { margin: 0; padding: 0; box-sizing: border-box; }
  html, body {
    width: 750px;
    height: 1200px;
    overflow: hidden;
    background: var(--page-bg);
  }
  .canvas {
    position: relative;
    width: 750px;
    height: 1200px;
  }
  .book {
    position: absolute;
    left: 70px;
    top: 40px;
    width: 645px;
    height: 1135px;
    filter: drop-shadow(10px 14px 16px rgba(0,0,0,0.28));
  }

  /* ---------- spine ---------- */
  .book-spine {
    position: absolute;
    left: 0;
    top: 6px;
    width: 84px;
    height: 1126px;
    overflow: hidden;
    background: linear-gradient(180deg, var(--spine-top) 0%, var(--spine-low) 60%, var(--sky-low) 100%);
  }
  .book-spine::after {
    content: "";
    position: absolute;
    inset: 0;
    background: linear-gradient(90deg, rgba(0,0,0,0.08) 0%, rgba(255,255,255,0.18) 30%, rgba(0,0,0,0) 60%, rgba(0,0,0,0.22) 100%);
    pointer-events: none;
  }
  .spine-title {
    position: absolute;
    top: 38px;
    left: 0;
    width: 100%;
    display: flex;
    justify-content: center;
    writing-mode: vertical-rl;
    font-family: "Noto Sans JP", sans-serif;
    font-weight: 900;
    font-size: 38px;
    line-height: 1;
    letter-spacing: 1px;
    color: var(--ink);
  }
  .spine-title .highlight { color: var(--accent-red); }
  .spine-title .spine-main {
    font-family: "Noto Serif JP", serif;
    margin-top: 16px;
    letter-spacing: 6px;
  }
  .spine-band {
    position: absolute;
    left: 0;
    bottom: 0;
    width: 100%;
    height: 330px;
    background: linear-gradient(180deg, var(--navy) 0%, var(--navy-deep) 100%);
    display: flex;
    justify-content: center;
    padding-top: 80px;
  }
  .spine-volume {
    writing-mode: vertical-rl;
    font-family: "Noto Serif JP", serif;
    font-weight: 900;
    font-size: 34px;
    letter-spacing: 20px;
    color: var(--white);
  }

  /* ---------- front cover ---------- */
  .book-cover {
    position: absolute;
    left: 84px;
    top: 0;
    width: 561px;
    height: 1135px;
    overflow: hidden;
    background: linear-gradient(180deg, var(--sky-top) 0%, var(--sky-mid) 30%, var(--sky-low) 45%);
  }
  .book-cover::before {
    content: "";
    position: absolute;
    left: 0;
    top: 0;
    width: 14px;
    height: 100%;
    background: linear-gradient(90deg, rgba(0,0,0,0.18), rgba(0,0,0,0));
    z-index: 5;
  }
  .series-title {
    position: absolute;
    top: 222px;
    left: 0;
    width: 100%;
    text-align: center;
    font-family: "Noto Sans JP", sans-serif;
    font-weight: 900;
    font-size: 47px;
    color: var(--ink);
  }
  .series-title .highlight { color: var(--accent-red); }
  .main-title-panel {
    position: absolute;
    top: 295px;
    left: 0;
    width: 100%;
    height: 120px;
    background: var(--panel-white);
    display: flex;
    align-items: center;
    justify-content: center;
  }
  .main-title {
    font-family: "Noto Serif JP", serif;
    font-weight: 900;
    font-size: 92px;
    letter-spacing: 2px;
    color: var(--ink);
  }
  .main-title .highlight { color: var(--accent-red); }
  .volume-label {
    position: absolute;
    top: 440px;
    left: 0;
    width: 100%;
    text-align: center;
    font-family: "Noto Serif JP", serif;
    font-weight: 900;
    font-size: 44px;
    letter-spacing: 16px;
    padding-left: 16px;
    color: var(--ink);
    z-index: 2;
  }
  .city-photo {
    position: absolute;
    top: 505px;
    left: 0;
    width: 100%;
    height: 400px;
    background: linear-gradient(180deg, rgba(238,246,252,0) 0%, var(--city-haze) 22%, var(--city-mid) 55%, var(--city-dark) 100%);
  }
  .tagline-band {
    position: absolute;
    left: 0;
    bottom: 0;
    width: 100%;
    height: 310px;
    background: linear-gradient(180deg, var(--navy) 0%, var(--navy-deep) 100%);
  }
  .tagline-band svg.band-edge {
    position: absolute;
    top: -34px;
    left: 0;
    width: 100%;
    height: 35px;
  }
  .subtitle-lead {
    position: absolute;
    top: 12px;
    left: 0;
    width: 100%;
    text-align: center;
    font-family: "Noto Serif JP", serif;
    font-weight: 900;
    font-size: 38px;
    color: var(--white);
  }
  .subtitle-main {
    position: absolute;
    top: 88px;
    left: 0;
    width: 100%;
    text-align: center;
    font-family: "Noto Sans JP", sans-serif;
    font-weight: 900;
    font-size: 54px;
    line-height: 90px;
    color: var(--white);
    transform: skewX(-10deg);
  }
  .subtitle-main .figure { font-size: 66px; }
</style>
</head>
<body>
  <main class="canvas">
    <div class="book">
      <aside class="book-spine">
        <p class="spine-title">
          <span>黄金<span class="highlight">羅針盤</span>アカデミー</span>
          <span class="spine-main">実践<span class="highlight">攻略</span></span>
        </p>
        <div class="spine-band">
          <span class="spine-volume">前編</span>
        </div>
      </aside>

      <article class="book-cover">
        <h2 class="series-title">黄金<span class="highlight">羅針盤</span>アカデミー</h2>
        <div class="main-title-panel">
          <h1 class="main-title">実践<span class="highlight">攻略</span></h1>
        </div>
        <p class="volume-label">前編</p>
        <div class="city-photo" role="img" aria-label="海沿いに高層ビルが立ち並ぶ都市の風景写真"></div>
        <section class="tagline-band">
          <svg class="band-edge" viewBox="0 0 561 35" preserveAspectRatio="none" aria-hidden="true">
            <path d="M0 35 Q280 0 561 35 Z" fill="#14244d"/>
          </svg>
          <p class="subtitle-lead">相続市場を狙え!!</p>
          <p class="subtitle-main">利回り<span class="figure">20%</span> &amp;<br>転売益<span class="figure">2000</span>万!</p>
        </section>
      </article>
    </div>
  </main>
</body>
</html>
```